I need a Professional Eye-Catching Paperback and e-Book Cover Design done with different mockups

I need a Professional Eye-Catching e-Book Cover Design done with different mockups

I need 2-3 designs to choose from per designer.

Book title - Lasting Harvest:

Subtitle - Growing riches beyond your years

Author name - K. Dapo Ramiro

I have attached some sample designs but i need you to be creative.

```html
<!DOCTYPE html>
<html lang="en">
<head>
<meta charset="UTF-8">
<title>Lasting Harvest — Book Cover</title>
<link rel="stylesheet" href="https://fonts.googleapis.com/css2?family=Oswald:wght@500&family=Open+Sans:wght@400&family=Montserrat:wght@500&display=swap">
<style>
  :root {
    --page-bg: #e9eaec;
    --cover-deep: #07131c;
    --cover-mid: #0f2a35;
    --cover-glow: #1b4a52;
    --gold-light: #f3d48a;
    --gold: #d6a94f;
    --gold-dark: #a77a2e;
    --teal-glow: #3fe0d0;
    --text-light: #eef2f2;
  }
  html, body {
    margin: 0;
    padding: 0;
    width: 1200px;
    height: 1200px;
    overflow: hidden;
    background: var(--page-bg);
  }
  .canvas {
    position: relative;
    width: 1200px;
    height: 1200px;
  }
  .book-cover {
    position: absolute;
    left: 222px;
    top: 60px;
    width: 756px;
    height: 1080px;
    background:
      radial-gradient(ellipse at 55% 55%, var(--cover-glow) 0%, var(--cover-mid) 40%, var(--cover-deep) 100%);
    box-shadow: 0 18px 40px rgba(0, 0, 0, 0.25);
    overflow: hidden;
  }
  .cover-title {
    position: absolute;
    left: 0;
    right: 0;
    top: 150px;
    margin: 0;
    text-align: center;
    font-family: 'Oswald', sans-serif;
    font-weight: 500;
    font-size: 104px;
    line-height: 1;
    letter-spacing: 1px;
    text-transform: uppercase;
    background: linear-gradient(180deg, var(--gold-light) 0%, var(--gold) 55%, var(--gold-dark) 100%);
    -webkit-background-clip: text;
    background-clip: text;
    color: transparent;
  }
  .cover-art {
    position: absolute;
    left: 178px;
    top: 330px;
    width: 400px;
    height: 460px;
  }
  .cover-subtitle {
    position: absolute;
    left: 0;
    right: 0;
    top: 848px;
    margin: 0;
    text-align: center;
    font-family: 'Open Sans', sans-serif;
    font-weight: 400;
    font-size: 34px;
    color: var(--text-light);
  }
  .cover-author {
    position: absolute;
    left: 0;
    right: 0;
    top: 952px;
    margin: 0;
    text-align: center;
    font-family: 'Montserrat', sans-serif;
    font-weight: 500;
    font-size: 34px;
    letter-spacing: 1px;
    text-transform: uppercase;
    color: var(--text-light);
  }
</style>
</head>
<body>
  <main class="canvas">
    <section class="book-cover">
      <h1 class="cover-title">Lasting Harvest</h1>
      <svg class="cover-art" viewBox="0 0 400 460" role="img" aria-label="Gold wireframe infinity symbol with glowing teal nodes">
        <defs>
          <radialGradient id="art-glow" cx="50%" cy="50%" r="50%">
            <stop offset="0%" stop-color="#3fe0d0" stop-opacity="0.35"/>
            <stop offset="55%" stop-color="#d6a94f" stop-opacity="0.12"/>
            <stop offset="100%" stop-color="#0f2a35" stop-opacity="0"/>
          </radialGradient>
        </defs>
        <ellipse cx="200" cy="230" rx="200" ry="230" fill="url(#art-glow)"/>
      </svg>
      <p class="cover-subtitle">Growing riches beyond your years</p>
      <p class="cover-author">K. Dapo Ramiro</p>
    </section>
  </main>
</body>
</html>
```